TRAILER DEIGNS

I NEED A DESIGN FOR MY TRAILER
7 FEET BY 14 FEET TRAILER

I ADDED A PICTURE OF MY TRUCK AS A SAMPLE I WANT TO KEEP IT SIMILAR

WEBSITE. BLUEPEAKROOFS.COM
4195550173

```html
<!DOCTYPE html>
<html lang="en">
<head>
<meta charset="utf-8">
<title>Bluepeak Exteriors – Trailer Wrap</title>
<link rel="stylesheet" href="https://fonts.googleapis.com/css2?family=Lato:wght@400;700;900&family=Oswald:wght@600&display=swap">
<style>
  :root {
    --sky-blue: #3aa8de;
    --ring-blue: #2a8fc2;
    --ink: #050505;
    --white: #ffffff;
    --badge-silver: #8a8f94;
    --badge-bronze: #6b4420;
    --badge-red: #d8312b;
  }
  * { box-sizing: border-box; margin: 0; padding: 0; }
  html, body { width: 1200px; height: 794px; overflow: hidden; background: #ffffff; }
  .wrap {
    position: relative;
    width: 1200px;
    height: 794px;
    font-family: "Lato", sans-serif;
    color: var(--white);
    overflow: hidden;
  }
  .wrap-shapes { position: absolute; inset: 0; }

  .brand { position: absolute; left: 50px; top: 150px; width: 330px; }
  .brand-name {
    display: flex; align-items: center; gap: 14px;
    font-weight: 900; font-size: 38px; line-height: 1.1; letter-spacing: 1px; text-transform: uppercase;
  }
  .brand-square { width: 30px; height: 30px; background: var(--sky-blue); flex: none; }
  .brand-rule { height: 6px; background: var(--sky-blue); margin: 20px 0 22px; width: 328px; }
  .brand-tagline { font-weight: 900; font-size: 22px; letter-spacing: 0.5px; word-spacing: 8px; }

  .service { position: absolute; top: 88px; width: 230px; text-align: center; }
  .service-photo {
    width: 220px; height: 220px; margin: 0 auto; border-radius: 50%;
    border: 9px solid var(--ring-blue);
    box-shadow: 6px 8px 14px rgba(0,0,0,0.25);
  }
  .service-photo.roof { background: linear-gradient(160deg, #7f9a6a 0%, #4c5560 45%, #3a4148 100%); }
  .service-photo.siding { background: linear-gradient(150deg, #d9d6cf 0%, #b8322e 55%, #e8e1cf 100%); }
  .service-photo.gutter { background: linear-gradient(160deg, #8b8a86 0%, #55585c 50%, #2f3a55 100%); }
  .service-label { margin-top: 40px; font-weight: 900; font-size: 42px; line-height: 1; letter-spacing: 0.5px; }
  .service.roofing { left: 471px; }
  .service.siding { left: 692px; }
  .service.gutters { left: 913px; }

  .partners { position: absolute; top: 462px; left: 530px; display: flex; align-items: center; gap: 22px; }
  .partner-divider { width: 2px; height: 80px; background: #555; }
  .badge-shield { width: 74px; height: 90px; background: var(--badge-silver); clip-path: polygon(0 0,100% 0,100% 80%,50% 100%,0 80%); }
  .badge-oval { width: 116px; height: 76px; border-radius: 50%; background: var(--badge-bronze); }
  .badge-square { width: 100px; height: 86px; background: var(--badge-red); }

  .contact-phone {
    position: absolute; left: 52px; top: 594px;
    font-family: "Oswald", sans-serif; font-weight: 600; font-size: 50px; line-height: 1;
    letter-spacing: -0.5px; white-space: nowrap;
  }
  .contact-web { position: absolute; left: 53px; top: 662px; font-size: 28px; font-weight: 400; line-height: 1; white-space: nowrap; }
  .contact-web b { font-weight: 700; }
  .license { position: absolute; left: 1010px; top: 642px; font-size: 18px; font-weight: 700; line-height: 1; }
</style>
</head>
<body>
<main class="wrap">
  <svg class="wrap-shapes" viewBox="0 0 1200 794" preserveAspectRatio="none" aria-hidden="true">
    <rect width="1200" height="794" fill="var(--sky-blue)"/>
    <ellipse cx="215" cy="200" rx="228" ry="245" fill="var(--ink)"/>
    <rect x="0" y="0" width="215" height="445" fill="var(--ink)"/>
    <path d="M190,452 C420,560 560,612 699,606 C900,598 1080,480 1200,340 L1200,372 C1080,500 900,620 699,628 C450,640 300,480 190,462 Z" fill="var(--white)"/>
    <path d="M0,466 C250,468 450,642 699,628 C900,620 1080,500 1200,372 L1200,794 L0,794 Z" fill="var(--ink)"/>
  </svg>

  <section class="brand">
    <div class="brand-name"><span class="brand-square"></span>Bluepeak Exteriors</div>
    <div class="brand-rule"></div>
    <p class="brand-tagline">ROOFING SIDING GUTTERS</p>
  </section>

  <section class="service roofing">
    <div class="service-photo roof" role="img" aria-label="Photo of roofers installing shingles on a house roof"></div>
    <p class="service-label">ROOFING</p>
  </section>
  <section class="service siding">
    <div class="service-photo siding" role="img" aria-label="Photo of a worker fitting siding panels to a wall"></div>
    <p class="service-label">SIDING</p>
  </section>
  <section class="service gutters">
    <div class="service-photo gutter" role="img" aria-label="Photo of a worker installing a rain gutter"></div>
    <p class="service-label">GUTTERS</p>
  </section>

  <section class="partners" aria-label="Partner badges">
    <div class="badge-shield"></div>
    <div class="partner-divider"></div>
    <div class="badge-oval"></div>
    <div class="partner-divider"></div>
    <div class="badge-square"></div>
  </section>

  <p class="contact-phone">419 . 555 . 0173</p>
  <p class="contact-web">www.<b>bluepeakroofs</b>.com</p>
  <p class="license">LIC# 207.548193</p>
</main>
</body>
</html>
```